Mini Book (4.25 x 6) Cover Design for Christian authors

We need a book cover designed for a mini book (4.25 x 6). We will need a front, back and spine for the book.
The book is titled:
Harbor Lanterns
Subtitle:
Quiet Light for Every Shore
Authors:
Walter and Renata Oskarsby
We are wanting the colors Dark Blue and Grey with more blue than grey.
We do not want any stock images or photos, only original work.
The cover should convey sincerity, intuition and truth with prestige.
We want the back cover text to be included (top) and the bios to be on the back as well (bottom). *Those documents are included in the files.
Since it is a mini book, it is important for the design to be simple and not cluttered, but powerful!
This is the first book in a twelve book series, so we would like the same "look" to carry through all twelve books, eventually.
On the back of the book, at the bottom (left), we want the following contact information:
Bright Meadow Method Logo (in files below)
tallwillowstudio@mailfernly.com
303.512.4086
P.O.Box 718
Larkfield, CO 80417

Please save room on the back (bottom-right) for the ISBN and price.
Updates

Thank you to the designers that have submitted feedback concerning our design brief. We have made some changes that will perhaps make it easier to submit a variety of designs.Thank you! Added Saturday, March 4, 2017

Target Market(s)

Christians - mainly women

Industry/Entity Type

Religious

Font styles to use
Serif
Sans Serif
Decorative
Script
Other font styles liked:
• Not any particular font, looking for one that goes well with the cover design.

Requirements
Must have
• Mini Book Size (4.25 x 6)-spine size 1/8" (0.125)
• Dark blue and grey colors
• Cover needs to be simple and not cluttered or busy.
• Intriguing
• A font that is attractive, but it is still easy to read.
• *File information below
Nice to have
• Designs that are different from the mainstream.
• Perhaps a design that would do something different with the title/font? Maybe a repeat of the words from smaller to larger? Not sure how it would look, but maybe?
Should not have
• Any other colors but dark blue and grey
• Cluttered Look

```html
<!DOCTYPE html>
<html lang="en">
<head>
<meta charset="utf-8">
<title>Harbor Lanterns – Cover Spread</title>
<link rel="stylesheet" href="https://fonts.googleapis.com/css2?family=Great+Vibes&family=Oswald:wght@300;400&family=Raleway:wght@600;700&display=swap">
<style>
  :root {
    --stage: #9b9b9b;
    --navy-deep: #0c1238;
    --navy: #1b2a6b;
    --navy-glow: #3b56a8;
    --slate: #a6aabb;
    --slate-dark: #7f8498;
    --ink-light: #ffffff;
    --glow: rgba(150, 185, 255, 0.9);
    --logo-ink: #2b2f7a;
  }
  * { margin: 0; padding: 0; box-sizing: border-box; }
  html, body { width: 1200px; height: 900px; overflow: hidden; }
  body {
    background: var(--stage);
    display: flex; align-items: center; justify-content: center;
    font-family: "Raleway", sans-serif;
  }
  .spread { display: flex; height: 780px; box-shadow: 0 10px 30px rgba(0,0,0,.35); }
  .panel {
    position: relative; width: 552px; height: 780px; overflow: hidden;
    background: radial-gradient(ellipse at 40% 45%, var(--navy-glow) 0%, var(--navy) 40%, var(--navy-deep) 100%);
    color: var(--ink-light);
  }
  .brush { position: absolute; inset: 0; width: 100%; height: 100%; }
  .back-copy { position: absolute; left: 44px; right: 40px; font-weight: 600; font-size: 13.5px; line-height: 1.3; }
  .back-intro { top: 44px; text-align: center; }
  .back-list { top: 196px; }
  .back-list ul { list-style: none; margin-top: 3px; }
  .back-list li { position: relative; padding-left: 20px; margin-bottom: 1px; }
  .back-list li::before { content: ""; position: absolute; left: 2px; top: 6px; width: 6px; height: 6px; border-radius: 50%; background: var(--ink-light); }
  .back-bio { top: 372px; text-align: center; }
  .back-quote { top: 500px; font-size: 15px; line-height: 1.4; }
  .contact { position: absolute; left: 60px; top: 668px; font-style: normal; font-weight: 700; font-size: 16px; line-height: 1.45; }
  .studio-mark {
    position: absolute; left: 368px; top: 612px; width: 160px; height: 100px;
    background: var(--ink-light); border-radius: 12px;
    display: flex; align-items: center; justify-content: center; gap: 8px;
    color: var(--logo-ink); font-weight: 700; font-size: 16px; line-height: 1.15; text-align: center;
  }
  .studio-mark::before { content: ""; width: 12px; height: 12px; border-radius: 50%; background: var(--logo-ink); flex: none; }
  .spine {
    width: 32px; height: 780px; background: linear-gradient(90deg, var(--navy-deep), var(--navy), var(--navy-deep));
    color: var(--ink-light); writing-mode: vertical-rl;
    display: flex; align-items: center; justify-content: space-between; padding: 18px 0 24px;
  }
  .spine-authors { font-family: "Oswald", sans-serif; font-size: 14px; }
  .spine-title { font-family: "Great Vibes", cursive; font-size: 26px; text-shadow: 0 0 6px var(--glow); }
  .cover-art {
    position: absolute; left: 58px; top: 62px; width: 410px; height: 410px; border-radius: 50%;
    background: radial-gradient(circle at 62% 42%, #e6ecf5 0%, #9fb4d6 35%, #2b3f7c 75%, #1a2558 100%);
  }
  .title {
    position: absolute; left: 0; right: 0; top: 440px; text-align: center;
    font-family: "Great Vibes", cursive; font-weight: 400; font-size: 86px; line-height: 1;
    text-shadow: 0 0 10px var(--glow), 0 0 22px var(--glow);
  }
  .subtitle {
    position: absolute; left: 0; right: 0; top: 545px; text-align: center;
    font-family: "Great Vibes", cursive; font-size: 38px;
    text-shadow: 0 0 8px var(--glow);
  }
  .authors {
    position: absolute; left: 0; right: 0; top: 660px; text-align: center;
    font-family: "Oswald", sans-serif; font-weight: 400; font-size: 28px; letter-spacing: -.3px;
  }
</style>
</head>
<body>
<main class="spread">
  <section class="panel back-cover">
    <svg class="brush" viewBox="0 0 552 780" preserveAspectRatio="none" aria-hidden="true">
      <polygon points="0,0 70,0 40,60 0,140" fill="var(--slate-dark)" opacity=".55"/>
      <polygon points="0,700 552,560 552,780 0,780" fill="var(--slate)"/>
      <polygon points="380,520 552,470 552,580 420,600" fill="var(--slate)" opacity=".8"/>
    </svg>
    <p class="back-copy back-intro">God always has our best interest at heart. Bright Meadow Method (BMM) gives us Strength, Confidence and Grit to persevere through the many challenges we face, and it prepares and propels us into our Divine Inheritance. By understanding the power that He has given to us, we are able to significantly impact the lives of others by fulfilling our own Blessed Destiny of being a blessing to others.</p>
    <div class="back-copy back-list">
      <p>This book will help you:</p>
      <ul>
        <li>Uncover the secret that is God’s plan</li>
        <li>Seek Divine revelation of the BMM for your specific situation</li>
        <li>Significantly impact the lives of others by fulfilling your own Blessed Destiny</li>
        <li>Discover the path you are meant to be on</li>
        <li>Recognize God’s imprint on your life and the importance of leaving your imprint on others</li>
      </ul>
    </div>
    <p class="back-copy back-bio">Renata and Walter Oskarsby are international award-winning authors who inspire couples and individuals to connect to the heart of God through Bright Meadow Method®. For over twenty years, they have conducted workshops and seminars throughout the country and at their private retreat center located in the Colorado mountains.</p>
    <blockquote class="back-copy back-quote">“Come, let us go up to the mountain of the LORD,<br>To the house (temple) of the God of Jacob;<br>That He may teach us His ways<br>And that we may walk in His paths.”<br>~ Isaiah 2:3~</blockquote>
    <div class="studio-mark">Tall Willow<br>Studio</div>
    <address class="contact">tallwillowstudio@mailfernly.com<br>303.512.4086<br>P.O.Box 718<br>Larkfield, CO 80417</address>
  </section>

  <aside class="spine">
    <span class="spine-authors">Walter and Renata Oskarsby</span>
    <span class="spine-title">Harbor Lanterns</span>
  </aside>

  <section class="panel front-cover">
    <svg class="brush" viewBox="0 0 552 780" preserveAspectRatio="none" aria-hidden="true">
      <polygon points="260,0 552,0 552,230 470,160" fill="var(--slate)" opacity=".85"/>
      <polygon points="0,430 200,360 240,480 0,600" fill="var(--slate)" opacity=".85"/>
    </svg>
    <div class="cover-art" role="img" aria-label="Circular illustration of a figure in prayer silhouetted against a pale moon, with a spiral and soft sparkling light"></div>
    <h1 class="title">Harbor Lanterns</h1>
    <p class="subtitle">Quiet Light for Every Shore</p>
    <p class="authors">Walter and Renata Oskarsby</p>
  </section>
</main>
</body>
</html>
```